Redesign Colorful Business Card

Please redesign the card attached. It is too busy. Please don't eliminate any of the words. The repetivite word "free" can be used less often.

Target Market(s)

College Students.

Contact Information for Business Card

The details listed in the attached image

Font styles to use
Sans Serif

Requirements
Must have
• A clear and simple presentation and must be attractive.

```html
<!DOCTYPE html>
<html lang="en">
<head>
<meta charset="utf-8">
<title>StudyBrisk Business Card</title>
<link rel="stylesheet" href="https://fonts.googleapis.com/css2?family=Roboto:wght@400;500&display=swap">
<style>
  :root {
    --page-bg: #e9ebe8;
    --panel-light: #c9e2c2;
    --panel-mid: #a9d2b3;
    --panel-left-a: #8fd3e8;
    --panel-left-b: #4dbd6a;
    --panel-left-c: #1e9a4a;
    --figure-a: #3f8a3a;
    --figure-b: #b7d631;
    --figure-c: #f4e622;
    --accent-yellow: #ffcc0a;
    --ink-dark: #1a1a1a;
    --ink-white: #ffffff;
  }
  * { margin: 0; padding: 0; box-sizing: border-box; }
  html, body {
    width: 1200px;
    height: 603px;
    overflow: hidden;
    background: var(--page-bg);
    font-family: "Roboto", Arial, sans-serif;
  }
  .stage {
    position: relative;
    width: 1200px;
    height: 603px;
  }
  .card {
    position: absolute;
    left: 110px;
    top: 20px;
    width: 696px;
    height: 399px;
    transform: scale(1.408);
    transform-origin: 0 0;
    overflow: hidden;
    box-shadow: 0 3px 10px rgba(0,0,0,0.18);
  }
  .card-art {
    position: absolute;
    inset: 0;
    width: 696px;
    height: 399px;
  }
  .web-band {
    position: absolute;
    left: 0;
    top: 358px;
    width: 330px;
    height: 41px;
    background: var(--accent-yellow);
  }
  .web-address {
    position: absolute;
    left: 36px;
    top: 360px;
    font-size: 30px;
    line-height: 36px;
    font-weight: 400;
    color: var(--ink-white);
    letter-spacing: 0.2px;
  }
  .benefits {
    position: absolute;
    left: 420px;
    top: 26px;
    width: 260px;
    text-align: center;
    color: var(--ink-white);
  }
  .benefit { margin-bottom: 11px; }
  .free-tag {
    display: inline-block;
    background: var(--accent-yellow);
    color: var(--ink-dark);
    font-size: 19px;
    line-height: 26px;
    padding: 0 7px;
    font-weight: 400;
  }
  .benefit-text {
    margin-top: 11px;
    font-size: 19.5px;
    line-height: 25px;
    letter-spacing: 0.6px;
    text-transform: uppercase;
  }
</style>
</head>
<body>
<main class="stage">
  <section class="card">
    <svg class="card-art" viewBox="0 0 696 399" xmlns="http://www.w3.org/2000/svg">
      <defs>
        <linearGradient id="rightPanelFill" x1="0" y1="0" x2="1" y2="1">
          <stop offset="0" stop-color="var(--panel-mid)"/>
          <stop offset="1" stop-color="var(--panel-light)"/>
        </linearGradient>
        <linearGradient id="leftPanelFill" x1="0" y1="0" x2="1" y2="1">
          <stop offset="0" stop-color="var(--panel-left-a)"/>
          <stop offset="0.55" stop-color="var(--panel-left-b)"/>
          <stop offset="1" stop-color="var(--panel-left-c)"/>
        </linearGradient>
        <linearGradient id="figureFill" x1="0" y1="0" x2="1" y2="0.4">
          <stop offset="0" stop-color="var(--figure-a)"/>
          <stop offset="0.5" stop-color="var(--figure-b)"/>
          <stop offset="1" stop-color="var(--figure-c)"/>
        </linearGradient>
      </defs>
      <rect class="right-panel" width="696" height="399" fill="url(#rightPanelFill)"/>
      <path class="divider-curve" d="M414 0 C334 40, 314 180, 374 260 S 364 380, 329 399"
            fill="none" stroke="var(--ink-white)" stroke-width="9"/>
      <path class="left-panel" d="M0 0 H408 C328 40, 308 180, 368 260 S 358 380, 323 399 H0 Z"
            fill="url(#leftPanelFill)"/>
      <rect class="mascot-illustration" role="img" aria-label="Faceted geometric elephant illustration raising its trunk"
            x="32" y="20" width="210" height="300" rx="40" fill="url(#figureFill)" opacity="0.9"/>
    </svg>
    <div class="web-band"></div>
    <p class="web-address">StudyBrisk.com</p>
    <div class="benefits">
      <div class="benefit">
        <span class="free-tag">FREE</span>
        <p class="benefit-text">Cut study time<br>down by up to 50%</p>
      </div>
      <div class="benefit">
        <span class="free-tag">FREE</span>
        <p class="benefit-text">Learn a dubject<br>without having to<br>go to class</p>
      </div>
      <div class="benefit">
        <span class="free-tag">FREE</span>
        <p class="benefit-text">Memorize<br>anything<br>quickly</p>
      </div>
    </div>
  </section>
</main>
</body>
</html>
```